Velmar Ops Business Cards

We need to design some upbeat business cards. We are an Industrial Rope Access Company/Height Safety Company that specialize in Rope Access, Confined Space, Anchor Points, Safety Systems, PPE Inspecions and Rigging.
Company name is Velmar Ops Ltd
Card is for Gareth Lomas the Company Director
His mobile number is 027 418 9072 and email is gareth@velmarops.co.nz. Website address is www.velmarops.co.nz.
We will post some pictures below to ensure you get a good idea of what we do.

```html
<!DOCTYPE html>
<html lang="en">
<head>
<meta charset="utf-8">
<title>Velmar Ops Business Cards</title>
<link rel="stylesheet" href="https://fonts.googleapis.com/css2?family=Arimo:wght@400;700&display=swap">
<style>
  :root {
    --backdrop: #9a9a9a;
    --card-white: #ffffff;
    --card-dark: #231f20;
    --card-dark-tint: #2e2a2b;
    --ink: #1a1a1a;
    --ink-soft: #333333;
    --light-text: #ffffff;
    --shadow: rgba(0, 0, 0, 0.45);
  }
  * { margin: 0; padding: 0; box-sizing: border-box; }
  html, body {
    width: 1200px;
    height: 900px;
    overflow: hidden;
    background: var(--backdrop);
    font-family: "Arimo", Arial, sans-serif;
  }
  .stage {
    position: relative;
    width: 1200px;
    height: 900px;
  }
  .card {
    position: absolute;
    top: 306px;
    width: 439px;
    height: 272px;
    border-radius: 11px;
    box-shadow: 2px 3px 3px var(--shadow);
    overflow: hidden;
  }
  .card-front {
    left: 149px;
    background: var(--card-white);
    color: var(--ink);
  }
  .card-back {
    left: 610px;
    background: var(--card-dark);
  }
  .wordmark {
    position: absolute;
    left: 0;
    right: 0;
    top: 78px;
    text-align: center;
    font-weight: 700;
    font-size: 38px;
    letter-spacing: 0.5px;
    color: var(--ink);
  }
  .identity {
    position: absolute;
    right: 240px;
    top: 185px;
    text-align: right;
  }
  .identity .person-name {
    font-weight: 700;
    font-size: 17px;
    letter-spacing: 0.3px;
    text-transform: uppercase;
    line-height: 20px;
  }
  .identity .person-role {
    font-size: 12.5px;
    color: var(--ink-soft);
    line-height: 15px;
  }
  .divider {
    position: absolute;
    left: 219px;
    top: 181px;
    width: 1px;
    height: 43px;
    background: var(--ink);
  }
  .contact-list {
    position: absolute;
    left: 231px;
    top: 179px;
    list-style: none;
    font-size: 12.5px;
    line-height: 16px;
    color: var(--ink);
  }
  .contact-list li {
    display: flex;
    align-items: center;
    gap: 4px;
  }
  .contact-list svg {
    width: 10px;
    height: 10px;
    fill: var(--ink);
    flex: none;
  }
  .back-pattern {
    position: absolute;
    inset: 0;
    background: linear-gradient(180deg, var(--card-dark-tint), var(--card-dark));
  }
  .back-wordmark {
    position: absolute;
    left: 236px;
    top: 131px;
    font-weight: 700;
    font-size: 21px;
    color: var(--light-text);
    letter-spacing: 0.3px;
  }
</style>
</head>
<body>
  <main class="stage">
    <section class="card card-front" aria-label="Business card front">
      <div class="wordmark">Velmar Ops</div>
      <div class="identity">
        <p class="person-name">Gareth Lomas</p>
        <p class="person-role">Director</p>
      </div>
      <div class="divider"></div>
      <ul class="contact-list">
        <li>
          <svg viewBox="0 0 10 10" aria-hidden="true"><path d="M1 3.5C1 2 2.5 1.2 5 1.2S9 2 9 3.5v.8H7V3.3H3v1H1z M2.2 5h5.6L9 8.8H1z"/></svg>
          027 418 9072
        </li>
        <li>
          <svg viewBox="0 0 10 10" aria-hidden="true"><path d="M1 2h8v6H1z" /><path d="M1 2l4 3.2L9 2" fill="none" stroke="#fff" stroke-width="0.9"/></svg>
          gareth@velmarops.co.nz
        </li>
        <li>
          <svg viewBox="0 0 10 10" aria-hidden="true"><circle cx="5" cy="5" r="4.3"/><path d="M3 3.2c1 .3 1.3 1.2 2.2 1.4M5.8 7.6c.2-1 1-1.3 1.8-1.6" fill="none" stroke="#fff" stroke-width="0.8"/></svg>
          www.velmarops.co.nz
        </li>
      </ul>
    </section>

    <section class="card card-back" aria-label="Business card back">
      <div class="back-pattern" role="img" aria-label="Faint repeated company name pattern across the dark background"></div>
      <div class="back-wordmark">Velmar Ops</div>
    </section>
  </main>
</body>
</html>
```